Unique Beautiful Realtor business card

I need a unique business card that includes my logo, my firms logo, my picture and phone number. The colors should compliment my logo.

Target Market(s)

People who want to buy or sell a home in South Florida

Contact Information for Business Card

Use two sides and work with the TMQ Coastal Dwellings logo as a theme.
The Dorsett Ambrose should be small and discreet, it is a requirement to be there but should be small. My photo should be integrated artistically.

Font styles to use
Serif
Sans Serif

Colors

Designer to choose colors to be used in the design.

Requirements
Must have
• My logo, Dorsett Ambrose logo, my photo, my phone number, (555-203-8846) and my website address. (www.tmqcoastaldwellings.example)
• Also my name, Marla J. Quenby, PA, Realtor
• Also “The Garden Minded Realtor”

```html
<!DOCTYPE html>
<html lang="en">
<head>
<meta charset="utf-8">
<title>TMQ Coastal Dwellings — Business Card</title>
<link rel="stylesheet" href="https://fonts.googleapis.com/css2?family=Roboto:wght@400;500;700&display=swap">
<style>
  :root {
    --backdrop: #5b6121;
    --card: #ffffff;
    --olive: #9ea535;
    --navy: #1d4582;
    --blue: #2c5fa3;
    --ink: #4a4a4a;
    --muted: #6a6a6a;
    --firm: #b31b34;
  }
  html, body {
    margin: 0;
    padding: 0;
    width: 1200px;
    height: 900px;
    overflow: hidden;
    background: var(--backdrop);
    font-family: "Roboto", Arial, sans-serif;
  }
  .canvas {
    position: relative;
    width: 1200px;
    height: 900px;
  }
  .card {
    position: absolute;
    left: 280px;
    width: 638px;
    height: 364px;
    background: var(--card);
    box-shadow: 0 4px 12px rgba(0,0,0,0.28);
    overflow: hidden;
  }
  .card--front { top: 69px; }
  .card--back { top: 463px; }

  .card-art {
    position: absolute;
    inset: 0;
    width: 638px;
    height: 364px;
  }

  .brand {
    position: absolute;
    display: flex;
    align-items: center;
    gap: 12px;
    color: var(--navy);
    font-weight: 700;
    white-space: nowrap;
  }
  .brand__mark {
    display: block;
    background: var(--olive);
  }
  .card--front .brand {
    left: 0;
    right: 0;
    top: 150px;
    justify-content: center;
    font-size: 32px;
    letter-spacing: 0.5px;
  }
  .card--front .brand__mark { width: 22px; height: 22px; }

  .front-url {
    position: absolute;
    right: 24px;
    top: 326px;
    color: #fff;
    font-size: 16px;
    white-space: nowrap;
  }

  .agent {
    position: absolute;
    left: 381px;
    top: 40px;
    width: 245px;
  }
  .card--back .brand {
    position: static;
    font-size: 19px;
    gap: 8px;
    margin-bottom: 58px;
  }
  .card--back .brand__mark { width: 14px; height: 14px; }

  .agent__name {
    margin: 0;
    font-size: 17px;
    font-weight: 500;
    color: var(--navy);
    letter-spacing: 0.3px;
    white-space: nowrap;
  }
  .agent__name .first { color: var(--olive); }
  .agent__title {
    margin: 4px 0 0;
    font-size: 13px;
    color: var(--muted);
  }
  .agent__motto {
    margin: 2px 0 0;
    font-size: 14px;
    color: var(--olive);
    white-space: nowrap;
  }
  .contact {
    list-style: none;
    margin: 20px 0 0;
    padding: 0;
    font-size: 14px;
    color: var(--ink);
  }
  .contact li {
    display: flex;
    align-items: center;
    gap: 7px;
    height: 23px;
    white-space: nowrap;
  }
  .contact .contact__phone { font-size: 16px; }
  .contact svg { width: 15px; height: 15px; flex: none; }

  .firm {
    margin-top: 22px;
    display: flex;
    align-items: center;
    gap: 6px;
    font-size: 11px;
    font-weight: 500;
    color: var(--muted);
    text-transform: uppercase;
    letter-spacing: 0.3px;
    white-space: nowrap;
  }
  .firm__mark {
    width: 10px;
    height: 10px;
    background: var(--firm);
  }
</style>
</head>
<body>
<main class="canvas">

  <section class="card card--front" aria-label="Card front">
    <svg class="card-art" viewBox="0 0 638 364" aria-hidden="true">
      <path class="wave-olive" d="M0 330 C180 340 300 305 420 312 C520 318 590 305 638 310 L638 364 L0 364 Z" fill="#9ea535"/>
      <path class="swoosh-navy" d="M0 290 C60 312 120 330 200 330 C250 330 290 326 310 324 C250 334 180 345 120 342 C70 340 30 330 0 322 Z" fill="#1d4582"/>
    </svg>
    <div class="brand">
      <span class="brand__mark"></span>
      <span class="brand__name">TMQ Coastal Dwellings</span>
    </div>
    <span class="front-url">www.tmqcoastaldwellings.example</span>
  </section>

  <section class="card card--back" aria-label="Card back">
    <svg class="card-art" viewBox="0 0 638 364">
      <defs>
        <linearGradient id="portraitTone" x1="0" y1="0" x2="0" y2="1">
          <stop offset="0" stop-color="#a9b7a0"/>
          <stop offset="0.35" stop-color="#c9b69a"/>
          <stop offset="0.6" stop-color="#8f9aa3"/>
          <stop offset="1" stop-color="#5d6670"/>
        </linearGradient>
      </defs>
      <path class="edge-olive" d="M280 0 L318 0 C296 80 300 150 312 220 C320 270 322 320 318 364 L290 364 Z" fill="#9ea535"/>
      <path class="edge-blue" d="M300 230 C318 270 322 320 318 364 L296 364 Z" fill="#2c5fa3"/>
      <path class="portrait" role="img" aria-label="Portrait photo of the realtor standing by a lakeside home"
            d="M0 0 L292 0 C282 80 288 150 296 220 C302 270 306 320 300 364 L0 364 Z"
            fill="url(#portraitTone)"/>
    </svg>

    <div class="agent">
      <div class="brand">
        <span class="brand__mark"></span>
        <span class="brand__name">TMQ Coastal Dwellings</span>
      </div>
      <h1 class="agent__name"><span class="first">MARLA J.</span> QUENBY</h1>
      <p class="agent__title">PA | Realtor</p>
      <p class="agent__motto">“The Garden Minded Realtor”</p>
      <ul class="contact">
        <li class="contact__phone">
          <svg viewBox="0 0 24 24" aria-hidden="true"><path fill="#1d4582" d="M6.6 10.8c1.4 2.8 3.8 5.1 6.6 6.6l2.2-2.2c.3-.3.7-.4 1-.2 1.1.4 2.3.6 3.6.6.6 0 1 .4 1 1V20c0 .6-.4 1-1 1C10.6 21 3 13.4 3 4c0-.6.4-1 1-1h3.5c.6 0 1 .4 1 1 0 1.3.2 2.5.6 3.6.1.3 0 .7-.2 1z"/></svg>
          <span>555 203 8846</span>
        </li>
        <li class="contact__web">
          <svg viewBox="0 0 24 24" aria-hidden="true"><circle cx="12" cy="12" r="9" fill="none" stroke="#1d4582" stroke-width="2.4"/><path d="M3 12h18M12 3c3 3 3 15 0 18M12 3c-3 3-3 15 0 18" fill="none" stroke="#1d4582" stroke-width="1.8"/></svg>
          <span>www.tmqcoastaldwellings.example</span>
        </li>
      </ul>
      <div class="firm">
        <span class="firm__mark"></span>
        <span>Harbor Point Dorsett Ambrose</span>
      </div>
    </div>
  </section>

</main>
</body>
</html>
```